Dental Office Business Card

We need a business card for our pediatric dentistry office.
On one side the design needs to contain the following:
our logo (attached)
Vento Pediatric Grins
Soraya Kadbelani, DDS
Board Certified Pediatric Dentist
Tel: (555) 318-2747)
Fax: (555) 264-8031
Email: info@ventopediatricgrins.example
Web: www.ventopediatricgrins.example
Address: 41 Brindle Ave, Suite 208, Wellesley, MA 02099

On the other side of the card, the design needs to have an appointment reminder (date and time as well as day of the week) similar to the design attached (no need for appointment reason “For”)

```html
<!DOCTYPE html>
<html lang="en">
<head>
<meta charset="utf-8">
<title>Vento Pediatric Grins – Business Card</title>
<link href="https://fonts.googleapis.com/css2?family=Montserrat:wght@400;500;600;700&family=Quicksand:wght@500;600&display=swap" rel="stylesheet">
<style>
  :root {
    --backdrop: #3a3a3a;
    --card: #ffffff;
    --card-shade: #f1f1f1;
    --ink: #1d1a1b;
    --muted: #4a4a4a;
    --mint: #8fd3a0;
    --mint-deep: #6cc085;
    --rule: #9a9a9a;
  }
  * { box-sizing: border-box; margin: 0; padding: 0; }
  html, body { width: 1200px; height: 900px; overflow: hidden; }
  body {
    background: var(--backdrop);
    font-family: "Montserrat", sans-serif;
    color: var(--ink);
    position: relative;
  }
  .card {
    position: absolute;
    left: 250px;
    width: 700px;
    height: 390px;
    border-radius: 36px;
    background: linear-gradient(135deg, var(--card-shade) 0%, var(--card) 45%, var(--card-shade) 100%);
    overflow: hidden;
  }
  .card--reminder { top: 40px; }
  .card--contact { top: 470px; }

  .brand {
    position: absolute;
    display: flex;
    align-items: center;
    gap: 12px;
  }
  .brand__dot {
    width: 34px; height: 34px;
    border-radius: 50%;
    background: var(--mint);
    flex: none;
  }
  .brand__name {
    font-family: "Montserrat", sans-serif;
    font-weight: 700;
    font-size: 28px;
    line-height: 1.1;
    color: var(--ink);
  }
  .card--reminder .brand { right: 48px; top: 40px; }
  .card--contact .brand { left: 44px; top: 150px; width: 300px; }
  .card--contact .brand__name { font-size: 26px; }

  .band-dark {
    position: absolute;
    left: 0; top: 300px;
    width: 590px; height: 48px;
    background: var(--ink);
    display: flex;
    align-items: center;
    justify-content: flex-end;
    padding-right: 40px;
    color: var(--mint);
  }
  .band-mint {
    position: absolute;
    left: 560px; right: 0;
    top: 260px; height: 40px;
    background: var(--mint);
  }

  .reminder__title {
    position: absolute;
    left: 60px; top: 128px;
    font-size: 20px;
    font-weight: 600;
  }
  .reminder__field {
    position: absolute;
    left: 60px;
    width: 500px;
    display: flex;
    align-items: flex-end;
    gap: 6px;
    font-size: 14px;
    font-weight: 500;
  }
  .reminder__field--date { top: 172px; }
  .reminder__field--time { top: 206px; }
  .reminder__line {
    flex: 1;
    border-bottom: 2px dotted var(--mint-deep);
    margin-bottom: 3px;
  }
  .reminder__days {
    position: absolute;
    left: 60px; top: 246px;
    display: flex;
    gap: 18px;
    list-style: none;
  }
  .reminder__day {
    display: flex;
    align-items: center;
    gap: 4px;
    font-size: 20px;
    font-weight: 500;
    color: var(--mint-deep);
  }
  .reminder__box {
    width: 14px; height: 14px;
    border: 1.5px solid var(--ink);
  }
  .reminder__web {
    font-family: "Quicksand", sans-serif;
    font-weight: 600;
    font-size: 15px;
    letter-spacing: 6px;
  }

  .contact__divider {
    position: absolute;
    left: 362px; top: 80px;
    width: 1.5px; height: 180px;
    background: var(--rule);
  }
  .contact__info {
    position: absolute;
    left: 385px; top: 78px;
  }
  .contact__name {
    font-size: 17px;
    font-weight: 500;
    color: var(--mint-deep);
    text-transform: uppercase;
  }
  .contact__title {
    font-size: 14px;
    font-weight: 500;
    color: var(--muted);
    margin-bottom: 14px;
  }
  .contact__list { list-style: none; }
  .contact__item {
    display: flex;
    align-items: center;
    gap: 8px;
    font-size: 14px;
    color: var(--muted);
    line-height: 24px;
  }
  .contact__item svg { width: 15px; height: 15px; flex: none; }
  .contact__address {
    font-family: "Quicksand", sans-serif;
    font-weight: 600;
    font-size: 17px;
    letter-spacing: 1px;
  }
</style>
</head>
<body>

<section class="card card--reminder" aria-label="Appointment reminder side">
  <div class="brand">
    <span class="brand__dot"></span>
    <span class="brand__name">Vento Pediatric Grins</span>
  </div>

  <h2 class="reminder__title">Appointment Reminder</h2>
  <div class="reminder__field reminder__field--date"><span>Date</span><span class="reminder__line"></span></div>
  <div class="reminder__field reminder__field--time"><span>Time(am./pm.)</span><span class="reminder__line"></span></div>

  <ul class="reminder__days">
    <li class="reminder__day"><span class="reminder__box"></span>Mon</li>
    <li class="reminder__day"><span class="reminder__box"></span>Tue</li>
    <li class="reminder__day"><span class="reminder__box"></span>Wed</li>
    <li class="reminder__day"><span class="reminder__box"></span>Thu</li>
    <li class="reminder__day"><span class="reminder__box"></span>Fri</li>
    <li class="reminder__day"><span class="reminder__box"></span>Sat</li>
    <li class="reminder__day"><span class="reminder__box"></span>Sun</li>
  </ul>

  <div class="band-mint"></div>
  <div class="band-dark"><span class="reminder__web">www.ventopediatricgrins.example</span></div>
</section>

<section class="card card--contact" aria-label="Contact side">
  <div class="brand">
    <span class="brand__dot"></span>
    <span class="brand__name">Vento Pediatric Grins</span>
  </div>

  <div class="contact__divider"></div>

  <div class="contact__info">
    <p class="contact__name">Soraya Kadbelani, DDS</p>
    <p class="contact__title">Board Certified Pediatric Dentist</p>
    <ul class="contact__list">
      <li class="contact__item">
        <svg viewBox="0 0 16 16" aria-hidden="true"><path d="M3 1.5l3 .5 1 3-1.8 1.3a9 9 0 0 0 4.5 4.5L11 9l3 1 .5 3-1.8 1.5C7 14 2 9 1.5 3.3z" fill="var(--mint-deep)"/></svg>
        <span>(555) 318-2747)</span>
      </li>
      <li class="contact__item">
        <svg viewBox="0 0 16 16" aria-hidden="true"><rect x="4" y="1.5" width="8" height="4" fill="none" stroke="var(--muted)" stroke-width="1.3"/><rect x="1.5" y="5.5" width="13" height="6" rx="1" fill="var(--muted)"/><rect x="4" y="10" width="8" height="4.5" fill="#fff" stroke="var(--muted)" stroke-width="1.3"/></svg>
        <span>(555) 264-8031</span>
      </li>
      <li class="contact__item">
        <svg viewBox="0 0 16 16" aria-hidden="true"><rect x="1" y="3" width="14" height="10" fill="var(--mint-deep)"/><path d="M1 3l7 6 7-6" fill="none" stroke="#fff" stroke-width="1.3"/></svg>
        <span>info@ventopediatricgrins.example</span>
      </li>
      <li class="contact__item">
        <svg viewBox="0 0 16 16" aria-hidden="true"><g fill="none" stroke="var(--mint-deep)" stroke-width="1.2"><circle cx="8" cy="8" r="6.5"/><ellipse cx="8" cy="8" rx="3" ry="6.5"/><path d="M1.5 8h13M2.5 4.8h11M2.5 11.2h11"/></g></svg>
        <span>www.ventopediatricgrins.example</span>
      </li>
    </ul>
  </div>

  <div class="band-mint"></div>
  <div class="band-dark"><span class="contact__address">41 Brindle Ave, Suite 208, Wellesley, MA 02099</span></div>
</section>

</body>
</html>
```